Business Card Design Project

I want a design for my business cards based on an excisting logo design.

Target Market(s)

Marketeers, PR-peeps, CEO's, decisionmakers, entrepreneurs

Industry/Entity Type

Business

Requirements
Nice to have
• Some visual interest on the back too
Should not have
• Sarif on the font

```html
<!DOCTYPE html>
<html lang="en">
<head>
<meta charset="utf-8">
<title>Sproutline Business Cards</title>
<link href="https://fonts.googleapis.com/css2?family=Arimo:wght@400;700&family=Questrial&display=swap" rel="stylesheet">
<style>
  :root {
    --stage: #3d3d3d;
    --card: #ffffff;
    --lime: #a3cc39;
    --leaf: #0f9b47;
    --pale: #e9f2d6;
    --ink: #555555;
    --muted: #9a9a9a;
  }
  * { margin: 0; padding: 0; box-sizing: border-box; }
  html, body { width: 1200px; height: 960px; overflow: hidden; }
  body { background: var(--stage); position: relative; font-family: "Arimo", Arial, sans-serif; }

  .card { position: absolute; background: var(--card); overflow: hidden; }

  /* Front side */
  .card-front { left: 340px; top: 134px; width: 564px; height: 341px; }
  .front-pattern { position: absolute; inset: 0; background: var(--pale); }
  .front-brand { position: absolute; left: 0; right: 0; top: 86px; text-align: center; }
  .front-brand .brand-dot { display: block; width: 96px; height: 96px; margin: 0 auto 10px; border-radius: 50%; background: var(--lime); }
  .front-brand .brand-name { font-family: "Questrial", Arial, sans-serif; font-size: 25px; color: var(--ink); letter-spacing: 1px; line-height: 1; }
  .front-brand .brand-web { margin-top: 4px; font-size: 16px; font-weight: 700; color: var(--lime); }

  /* Back side */
  .card-back { left: 340px; top: 515px; width: 571px; height: 343px; }
  .back-brand .brand-dot { position: absolute; left: 72px; top: 92px; width: 108px; height: 108px; border-radius: 50%; background: var(--lime); }
  .back-brand .brand-name { position: absolute; left: 42px; top: 207px; font-family: "Questrial", Arial, sans-serif; font-size: 25px; color: var(--ink); letter-spacing: 1px; }

  .person { position: absolute; left: 332px; top: 72px; width: 220px; }
  .person-name { font-size: 22px; color: var(--lime); line-height: 1; }
  .person-name .surname { color: var(--leaf); }
  .person-rule { height: 1px; margin-top: 7px; background: linear-gradient(to right, #cfcfcf, rgba(207,207,207,0)); }
  .person-role { margin: 6px 0 0 63px; font-size: 12px; color: var(--muted); }

  .contacts { position: absolute; left: 268px; top: 167px; list-style: none; }
  .contacts li { position: relative; padding-left: 25px; font-size: 12px; line-height: 15px; color: var(--ink); margin-bottom: 4px; }
  .contacts li.phone { margin-top: 6px; }
  .contacts svg { position: absolute; left: 0; top: 1px; width: 12px; height: 12px; fill: var(--leaf); }

  .band { position: absolute; left: 0; right: 0; bottom: 0; height: 27px; background: var(--lime); }
  .band-tab { position: absolute; right: 0; bottom: 0; width: 122px; height: 33px; background: var(--leaf); border-top-left-radius: 12px; }
</style>
</head>
<body>

  <section class="card card-front">
    <div class="front-pattern" role="img" aria-label="Repeating pattern of pale green brand marks across the card"></div>
    <div class="front-brand">
      <span class="brand-dot"></span>
      <p class="brand-name">Sproutline</p>
      <p class="brand-web">www.sproutline.com</p>
    </div>
  </section>

  <section class="card card-back">
    <div class="back-brand">
      <span class="brand-dot"></span>
      <p class="brand-name">Sproutline</p>
    </div>

    <div class="person">
      <p class="person-name">Marco <span class="surname">Elwin</span></p>
      <div class="person-rule"></div>
      <p class="person-role">Manager</p>
    </div>

    <ul class="contacts">
      <li>
        <svg viewBox="0 0 12 12" aria-hidden="true"><path d="M6 1 L11 6 H9.5 V11 H7 V8 H5 V11 H2.5 V6 H1 Z"/></svg>
        45 Linden Avenue, 9th Floor<br>Linden House
      </li>
      <li class="phone">
        <svg viewBox="0 0 12 12" aria-hidden="true"><path d="M2.5 1 L4.5 1 L5.2 3.6 L4 4.6 C4.7 6.2 5.8 7.3 7.4 8 L8.4 6.8 L11 7.5 L11 9.5 C11 10.4 10.3 11 9.5 11 C5 10.7 1.3 7 1 2.5 C1 1.7 1.6 1 2.5 1 Z"/></svg>
        0100 555 010 200
      </li>
      <li>
        <svg viewBox="0 0 12 12" aria-hidden="true"><path d="M1 3 H11 V10 H1 Z M1.6 3.4 L6 7 L10.4 3.4" /></svg>
        marco@sproutline.com
      </li>
      <li>
        <svg viewBox="0 0 12 12" aria-hidden="true"><circle cx="6" cy="6" r="5"/></svg>
        www.sproutline.com
      </li>
    </ul>

    <div class="band"></div>
    <div class="band-tab"></div>
  </section>

</body>
</html>
```